Beauty Therapy Web Design

I need a web page design for a small beauty therapy clinic, the owner is currently the only beauty therapist working there.
We require the following pages:
Home
About
Treatments
Nails
Courses
Contact
I will attach the clinics business card, treatment menu and signage so that you get a feeling for the branding colours etc.
This is the first website for the beauty therapist, she would like to attract new clients and also tourists that come in on the cruise ships. The thing that sets her apart from other clinics is that she welcomes texting for appointments.
I have selected refundable because I have never done this before so I don't know what to expect, I have the full intention of going through with it as long as I get a good design.
Feel free to ask for further information
Reason: Project extended as I am away for work and am unable to meet with the owner.
Target Market(s)
Females 18 to 50
Industry/Entity Type
Business
Look and feel
Each slider illustrates characteristics of the customer's brand and the style your logo design should communicate.

```html
<!DOCTYPE html>
<html lang="en">
<head>
<meta charset="utf-8">
<title>Solenne Beauty Therapy – About Us</title>
<link rel="stylesheet" href="https://fonts.googleapis.com/css2?family=PT+Sans:wght@400;700&display=swap">
<style>
  :root {
    --top-bar: #1d1d1d;
    --page-bg: #ffffff;
    --panel: #efede9;
    --band: #8c739f;
    --nav-link: #a98dbf;
    --nav-active-bg: #d6d3d0;
    --nav-active-text: #ffffff;
    --heading: #3d1248;
    --body-text: #111111;
    --scroll-track: #d6d2ce;
    --scroll-thumb: #9b3fc4;
    --footer-grey: #9a9a9a;
    --brand: #8a6a2a;
  }
  * { margin: 0; padding: 0; box-sizing: border-box; }
  html, body { width: 1200px; height: 675px; overflow: hidden; }
  body { font-family: "PT Sans", Tahoma, sans-serif; background: var(--page-bg); }
  .canvas { position: relative; width: 1200px; height: 675px; overflow: hidden; background: var(--page-bg); }
  .top-bar { position: absolute; left: 0; top: 0; width: 1200px; height: 50px; background: var(--top-bar); }
  .bottom-band { position: absolute; left: 0; top: 587px; width: 1200px; height: 88px; background: var(--band); }
  .hero-photo { position: absolute; left: 0; top: 50px; width: 1200px; height: 537px; }
  .content-panel { position: absolute; left: 672px; top: 50px; width: 528px; height: 537px;
    background: linear-gradient(90deg, rgba(239,237,233,0.88), var(--panel) 20%); }
  .brand { position: absolute; left: 26px; top: 78px; width: 202px; display: flex; align-items: center; gap: 8px;
    color: var(--brand); font-weight: 700; font-size: 21px; line-height: 1.1; }
  .brand-mark { width: 14px; height: 14px; background: var(--brand); flex: none; }
  .main-nav { position: absolute; left: 23px; top: 157px; width: 205px; list-style: none; }
  .main-nav li { height: 28.7px; }
  .main-nav a { display: block; padding-left: 9px; font-size: 16px; line-height: 28.7px; color: var(--nav-link); text-decoration: none; }
  .main-nav .is-active a { background: var(--nav-active-bg); color: var(--nav-active-text); height: 37px; line-height: 37px; }
  .main-nav .is-active { height: 34px; }
  .footer-links { position: absolute; left: 22px; top: 549px; display: flex; align-items: center; gap: 12px; }
  .social-square { width: 12px; height: 13px; background: var(--footer-grey); }
  .footer-links span { font-size: 11px; color: var(--footer-grey); letter-spacing: 0.2px; }
  .footer-rule { position: absolute; left: 22px; top: 569px; width: 156px; height: 1px; background: #cfcfcf; }
  .about-title { position: absolute; left: 706px; top: 137px; font-size: 24px; font-weight: 400; color: var(--heading); }
  .about-text { position: absolute; left: 700px; top: 196px; width: 434px; height: 360px; overflow: hidden;
    font-size: 11px; line-height: 11.9px; color: var(--body-text); text-align: justify; hyphens: auto; }
  .about-text p { margin-bottom: 14px; }
  .about-text p + p + p { margin-top: 14px; }
  .scroll-track { position: absolute; left: 1149px; top: 155px; width: 10px; height: 401px; background: var(--scroll-track); }
  .scroll-thumb { position: absolute; left: 0; top: 0; width: 10px; height: 90px; background: var(--scroll-thumb); }
</style>
</head>
<body>
<div class="canvas">
  <div class="top-bar"></div>

  <svg class="hero-photo" width="1200" height="537" viewBox="0 0 1200 537" role="img" aria-label="Portrait photograph of a young woman with long brown hair, resting her chin on her bare shoulder">
    <defs>
      <linearGradient id="heroTones" x1="0" y1="0" x2="1" y2="0.4">
        <stop offset="0" stop-color="#f4efea"/>
        <stop offset="0.35" stop-color="#d8b8a0"/>
        <stop offset="0.7" stop-color="#8a6148"/>
        <stop offset="1" stop-color="#c9b2a0"/>
      </linearGradient>
    </defs>
    <polygon points="285,0 672,0 672,537 195,537" fill="url(#heroTones)"/>
  </svg>

  <div class="content-panel"></div>
  <div class="bottom-band"></div>

  <div class="brand"><span class="brand-mark"></span>Solenne Beauty Therapy</div>

  <ul class="main-nav">
    <li class="is-active"><a href="#">Home</a></li>
    <li><a href="#">About</a></li>
    <li><a href="#">Treatments</a></li>
    <li><a href="#">Nails</a></li>
    <li><a href="#">Courses</a></li>
    <li><a href="#">Contact</a></li>
  </ul>

  <div class="footer-links">
    <div class="social-square"></div>
    <div class="social-square"></div>
    <span>CONTACT</span>
    <span>PRESS</span>
  </div>
  <div class="footer-rule"></div>

  <h1 class="about-title">About Us</h1>
  <div class="about-text">
    <p>Lorem Ipsum is simply dummy text of the printing and typesetting industry. Lorem Ipsum has been the industry's standard dummy text ever since the 1500s, when an unknown printer took a galley of type and scrambled it to make a type specimen book. It has survived not only five centuries, but also the leap into electronic typesetting, remaining essentially unchanged. It was popularised in the 1960s with the release of Typeline sheets containing Lorem Ipsum passages, and more recently with desktop publishing software like Folio PageSetter including versions of Lorem Ipsum.</p>
    <p>It is a long established fact that a reader will be distracted by the readable content of a page when looking at its layout. The point of using Lorem Ipsum is that it has a more-or-less normal distribution of letters, as opposed to using 'Content here, content here', making it look like readable English. Many desktop publishing packages and web page editors now use Lorem Ipsum as their default model text, and a search for 'lorem ipsum' will uncover many web sites still in their infancy. Various versions have evolved over the years, sometimes by accident, sometimes on purpose (injected humour and the like).</p>
    <p>Contrary to popular belief, Lorem Ipsum is not simply random text. It has roots in a piece of classical Latin literature from 45 BC, making it over 2000 years old. Martin Hale, a Latin professor at Ashbury College in Virginia, looked up one of the more obscure Latin words, consectetur, from a Lorem Ipsum passage, and going through the cites of the word in classical literature, discovered the undoubtable source. Lorem Ipsum comes from sections 1.10.32 and 1.10.33 of "de Finibus Bonorum et Malorum" (The Extremes of Good and Evil) by Tullan, written in 45 BC. This book is a treatise on the theory of ethics, very popular during the Renaissance. The first line of Lorem Ipsum, "Lorem ipsum dolor sit amet..", comes from a line in section 1.10.32.</p>
  </div>

  <div class="scroll-track"><div class="scroll-thumb"></div></div>
</div>
</body>
</html>
```